English and Spanish Language School Needs a Business Card

Need a business card design a startup company called Corvelle Language School. The company will offer English and Spanish conversational level courses designed to make the learner feel comfortable with grammar and vocabulary. We would like to see a logo with some colour that should communicate learning, growth.

Target Market(s)

Consumers and businesses

Industry/Entity Type

Education

Contact Information for Business Card

TBD

Font styles to use
Serif

Requirements
Must have
• Include the following
• Logo
• Name
• Title
• Cellphone Number
• Office Phone number
• Email address
• Office Address

```html
<!DOCTYPE html>
<html lang="en">
<head>
<meta charset="utf-8">
<title>Corvelle Language School – Business Card</title>
<link rel="stylesheet" href="https://fonts.googleapis.com/css2?family=Open+Sans:wght@400;600;700&display=swap">
<style>
  :root {
    --brand-red: #c1272d;
    --brand-teal: #1fa3a6;
    --card-cream: #efece2;
    --ink: #4a4440;
    --divider: #cfc9bd;
    --backdrop: #dcdcdc;
  }
  * { box-sizing: border-box; margin: 0; padding: 0; }
  html, body { width: 1200px; height: 786px; overflow: hidden; }
  body {
    background: var(--backdrop);
    font-family: "Open Sans", Arial, sans-serif;
    position: relative;
  }
  .card {
    position: absolute;
    top: 238px;
    width: 540px;
    height: 309px;
    border-radius: 18px;
    overflow: hidden;
    box-shadow: 0 6px 18px rgba(0,0,0,.18);
  }
  .card--front { left: 40px; background: var(--card-cream); }
  .card--back  { left: 620px; background: var(--brand-red); }

  .wave { position: absolute; left: 0; top: 0; width: 540px; height: 309px; }

  .wordmark {
    position: absolute;
    font-weight: 700;
    line-height: 1.05;
  }
  .card--front .wordmark {
    left: 44px; top: 92px; width: 220px;
    font-size: 30px; color: var(--brand-red);
  }
  .card--back .wordmark {
    left: 46px; top: 96px; width: 260px;
    font-size: 38px; color: var(--card-cream);
  }

  .divider {
    position: absolute; left: 292px; top: 62px;
    width: 1px; height: 176px; background: var(--divider);
  }

  .contact { position: absolute; left: 312px; top: 66px; color: var(--ink); }
  .contact__name {
    font-size: 17px; font-weight: 700; color: var(--brand-red);
    letter-spacing: .5px; text-transform: uppercase;
  }
  .contact__title { font-size: 13px; margin-bottom: 12px; }
  .contact__list { list-style: none; font-size: 12.5px; }
  .contact__list li { display: flex; align-items: center; gap: 7px; height: 19px; }
  .contact__icon {
    width: 13px; height: 13px; border-radius: 3px;
    background: var(--brand-red); flex: none;
  }
  .contact__address { font-size: 12.5px; margin-top: 8px; line-height: 1.5; }

  .accent-circle {
    position: absolute; right: -40px; bottom: -70px;
    width: 250px; height: 250px; border-radius: 50%;
    background: var(--brand-teal);
  }
</style>
</head>
<body>

<section class="card card--front" aria-label="Business card front">
  <svg class="wave" viewBox="0 0 540 309" aria-hidden="true">
    <path d="M0 190 C90 215 180 250 250 309 L0 309 Z" fill="var(--brand-red)"/>
    <path d="M0 180 C95 206 190 245 262 309" fill="none" stroke="var(--card-cream)" stroke-width="6"/>
    <path d="M0 172 C100 198 200 240 276 309" fill="none" stroke="var(--brand-teal)" stroke-width="4"/>
  </svg>

  <div class="wordmark">Corvelle Language School</div>
  <div class="divider"></div>

  <div class="contact">
    <div class="contact__name">Mara Linwood</div>
    <div class="contact__title">General Manager</div>
    <ul class="contact__list">
      <li><svg class="contact__icon" viewBox="0 0 13 13" aria-hidden="true"><rect width="13" height="13" rx="3" fill="var(--brand-red)"/><rect x="4" y="2" width="5" height="9" rx="1" fill="none" stroke="#fff" stroke-width="1.2"/></svg>555-014-2286</li>
      <li><svg class="contact__icon" viewBox="0 0 13 13" aria-hidden="true"><rect width="13" height="13" rx="3" fill="var(--brand-red)"/><path d="M4 3 L5.5 3 L6 5 L5 6 C5.6 7.2 6 7.6 7 8 L8 7 L10 7.5 L10 9 C7 9.5 3.5 6 4 3Z" fill="#fff"/></svg>555-014-2287</li>
      <li><svg class="contact__icon" viewBox="0 0 13 13" aria-hidden="true"><rect width="13" height="13" rx="3" fill="var(--brand-red)"/><rect x="2.5" y="3.5" width="8" height="6" fill="none" stroke="#fff" stroke-width="1.1"/><path d="M2.5 3.5 L6.5 7 L10.5 3.5" fill="none" stroke="#fff" stroke-width="1.1"/></svg>info@corvellels.com</li>
      <li><svg class="contact__icon" viewBox="0 0 13 13" aria-hidden="true"><rect width="13" height="13" rx="3" fill="var(--brand-red)"/><circle cx="6.5" cy="6.5" r="4" fill="none" stroke="#fff" stroke-width="1.1"/><path d="M2.5 6.5 H10.5 M6.5 2.5 V10.5" stroke="#fff" stroke-width="1"/></svg>www.corvellels.com</li>
    </ul>
    <div class="contact__address">48 Harlow St. Suite 305<br>Brookfield ME 04011</div>
  </div>
</section>

<section class="card card--back" aria-label="Business card back">
  <div class="wordmark">Corvelle Language School</div>
  <div class="accent-circle"></div>
</section>

</body>
</html>
```